Business Cards for 41Vale

I need business cards that goes with the logo
Updates

Dear designers - many thanks for the responsesreceived to date. There are many good designs but most of them are landscape.Could you please submit a few options for portrait layout as well.

Industry/Entity Type

Business

```html
<!DOCTYPE html>
<html lang="en">
<head>
<meta charset="utf-8">
<title>41Vale Business Card</title>
<link href="https://fonts.googleapis.com/css2?family=Michroma&display=swap" rel="stylesheet">
<style>
  :root {
    --canvas-bg: #dcdcdc;
    --card-bg: #ffffff;
    --card-edge: #d4d4d4;
    --band: #50555b;
    --band-text: #ffffff;
    --band-subtle: #c9ccd0;
    --brand-grey: #50555b;
  }
  * { margin: 0; padding: 0; box-sizing: border-box; }
  html, body {
    width: 1200px; height: 765px; overflow: hidden;
    background: var(--canvas-bg);
    font-family: "Michroma", sans-serif;
  }
  .canvas { position: relative; width: 1200px; height: 765px; }
  .card {
    position: absolute; top: 302px; width: 575px; height: 343px;
    background: var(--card-bg);
    border: 1px solid var(--card-edge);
    border-radius: 40px; overflow: hidden;
  }
  .card--front { left: 16px; }
  .card--back { left: 604px; }
  .front-wordmark {
    position: absolute; left: 0; right: 0; top: 142px;
    text-align: center; font-size: 44px; line-height: 1;
    color: var(--brand-grey); letter-spacing: 0;
  }
  .contact-band {
    position: absolute; left: 0; right: 0; top: 133px; height: 112px;
    background: var(--band); color: var(--band-text);
  }
  .holder { position: absolute; left: 56px; top: 42px; }
  .holder-name { font-size: 17px; line-height: 1; letter-spacing: 0.5px; }
  .holder-role { font-size: 8px; margin-top: 4px; color: var(--band-subtle); letter-spacing: 0.5px; }
  .band-divider {
    position: absolute; left: 201px; top: 16px; width: 1px; height: 80px;
    background: var(--band-subtle);
  }
  .contact-list { position: absolute; left: 211px; top: 26px; list-style: none; }
  .contact-item {
    display: flex; align-items: center; gap: 6px;
    font-size: 9.5px; height: 17.5px; letter-spacing: 0.6px;
  }
  .contact-item svg { width: 12px; height: 10px; fill: var(--band-text); flex: none; }
  .band-wordmark {
    position: absolute; left: 452px; top: 47px;
    font-size: 15px; line-height: 1; color: var(--band-text);
  }
</style>
</head>
<body>
<main class="canvas">
  <section class="card card--front" aria-label="Card front">
    <div class="front-wordmark">41Vale</div>
  </section>

  <section class="card card--back" aria-label="Card back">
    <div class="contact-band">
      <div class="holder">
        <div class="holder-name">ALAN REED</div>
        <div class="holder-role">PRESIDENT</div>
      </div>
      <div class="band-divider"></div>
      <ul class="contact-list">
        <li class="contact-item">
          <svg viewBox="0 0 12 10" aria-label="Phone"><path d="M1 3 Q6 0 11 3 L10 5 L8 4 L8 3 Q6 2 4 3 L4 4 L2 5 Z"/><rect x="3" y="5" width="6" height="4" rx="1"/></svg>
          00 321 7654 098
        </li>
        <li class="contact-item">
          <svg viewBox="0 0 12 10" aria-label="Fax"><rect x="3" y="0" width="6" height="3"/><rect x="1" y="3" width="10" height="5" rx="1"/><rect x="3" y="7" width="6" height="3"/></svg>
          00 321 7654 098
        </li>
        <li class="contact-item">
          <svg viewBox="0 0 12 10" aria-label="Email"><path d="M1 1 H11 V9 H1 Z M1.5 1.5 L6 5.5 L10.5 1.5" stroke="#50555b" stroke-width="0.8"/></svg>
          ALANREED@41VALE.COM
        </li>
      </ul>
      <div class="band-wordmark">41Vale</div>
    </div>
  </section>
</main>
</body>
</html>
```